Mobile Application for Friend Tagging: "Pick the Pal" (A.k.a.: PalPick / PP)

Introduction
We need an app design called "PalPick" for both iOS and Android. The theme of the application is Friend Tagging, and basically it adopts the endorsement mechanism similar to Corvano.
Summary
A typical example usage scenario starts as follows: User logs in with Trellisa account and activity feed screen appears. On activity screen, friend activity such as "Friend A endorsed Friend B for personal trait X", or "Friend C voted `yes` for this endorsement" or "6 friends voted `nay` for another endorsement", etc, is displayed.
Once the user taps any of the activity feed, the user can join the survey where Friend A is voted for some personal trait. Voting screen is a dedicated screen for this task where user can vote 'yea' or 'nay' for a given endorsement survey. Small fragments of information such as percentage of 'yea' votes or 'friends who voted for this' can also be displayed on this screen.
There are two types of endorsing a person: Users can either join an existing character survey or he/she can define a new personal trait and tag the person of interest. The process of defining a new trait is called 'Revealing'.
Revealing consists of three steps all of which correspond to a particular screen. In the first step, user chooses a category for the personal trait. There are currently six categories: Relations, Social, Technical, At Home, Sports and Outdoors. Once the category is chosen, second step of `reveal` process appears. Here, user can either choose traits from the list provided or he/she can type a new trait. Finally, in the 3rd screen of 'reveal' process, user can place a positive or negative vote on the endorsement he created.
The core concept of the application is explained above. Remaining screens such as detail profile screen, settings, notifications, friends, sliding pane, are supplementary and self explanatory.
We are expecting,
Multiple design alternatives with different design approaches, different layouts and different colour palettes for:
A) A logo including "PalPick" text.or any other freeform creative logo design.
B) 13 screens whose prototypes are provided in the attachment.
C) 29 Icons included in screen design.
For each screen we expect the following resolutions:
1024 x 600 (Standard netbook/tablet resolution)
1280 x 800 (Norvex Tablets)
1024x768 (Quillo Slate Petite)
640×1136 (Quillo Handy 5, 5S & 5C)
Design Requirements for each screen is explained below in detail:
1 - Splash Screen
Requirements:
- Includes Logo.
Our Inspirations for this screen:
- http://www.screenfolio-example.net/splash-screens,
- Attachment File 15: Splash_Screen (1)
2 - Sign Up Screen
Requirements:
- Includes Trellisa Login only.
- We would love to see a stylish drawing or GIF here.
- Attachment File 16: Sign_Up (2)
- http://www.screenfolio-example.net/sign-up-flows
3 - Activity Feed
Requirements:
- A quick vote section similar to one drawn in: File 1: Activity_Feed (3)
- http://www.screenfolio-example.net/feeds
4 - Profile Summary Screen:
Requirements:
- Summary visualisation of all endorsements in a suitable format which designer can choose.
- A quick vote section (Similar to the voting box in the middle seen in: File 6: - Profile_(Friend)_v1 (6)
-Vote Now button. Required to have plenty of emphasise.
- http://www.screenfolio-example.net/user-profiles
- File 6: Profile_(Friend)_v1 (6)
- File 7: Profile_(Non_Friend) (4)
- File 9: Profile_(Friend)_v2 (7)
- File 18: Profile_(Friend)_v3 (7)
5 - Detail Profile
Requirements:
- List View Screen where each row should contain the following:
- Positive and Negative voting buttons if given detail profile view belongs to a friend.
- A horizontal bar indicating the percentage of yes&no votes.
- Profile screen aligned to left
- Multiple small thumbnails view.
- Hide button if profile belongs to user himself/herself.
- File 2: Detail_Profile_(Non_Friend) (5)
- File 3: Detail_Profile_(Self) (9)
- File 4: Detail_Profile_(Friend) (8)
6 - Reveal 1/3 Screen (Select Category Screen)
Requirements:
- 6 major categories have buttons placed in a compact button set.
- A step definitions view describing 3 steps included in new trait creation process.
- File 8: Reveal_13 (10)
7 - Reveal 2/3 Screen (Reveal It! Screen)
Requirements:
- Text field with search-as-you-type view
- Visualisation of available traits so that user can either type a trait or pick one.
- File 10: Reveal_23_Keyboard_Hidden (11)
- File 11: Reveal_23_Keyboard_Visible (12)
- http://www.screenfolio-example.net/compose-screens
8 - Reveal 3/3 Screen (End)
Requirements:
This page should be directly encouraging users to vote.
http://img0.screenfolio-example.net/img/full/1380652995164-2013-09-26%2021.17.38.png
File 14: Reveal_33 (13)
9 - Vote Screen
Requirements:
File 17: Vote (14)
10 - Sliding Panel
Requirements:
There should be five rows: Home - Friends - Add Friends - About - Settings
Each menu item should have its own icon.
http://www.screenfolio-example.net/custom-navigation
File 13: Sliding_Panel (15)
11 - Notifications Screen:
Requirements:
This is a list screen so we need a row design here.
There are two types of notifications, thus two types of rows. First type notifies for an endorsement. It should have the text: "Friend X voted for a trait: Y", Friend's Thumbnail picture and a icon on the right side, indicating the action for "hiding trait from timeline".
Second type is Friendship request notification. It has the text: "X send you a friendship request". It should have Friend's Thumbnail picture and a icon on the right side, indicating the action for "accept request".
File 5: Notifications (16)
12 - Settings Screen:
Requirements:
This screen is supposed to be a native looking customisation screen.
It should have two main sections: PRIVACY and SUPPORT. Privacy section should contain a switch for stealth mode, which helps users to hide some content. There should be a logo for stealth mode.
Support section should have three options: "Privacy Policy", "Terms of Service" and "Report a Bug"
File 12: Settings (17)
C) Icons
Here we list the names of icons required for each page:
Page 3:
- Header Bar Search Icon
- Header Bar Notifications Icon
- Header Bar Sliding Panel Icon
- Double Chevron Left Icon
- Double Chevron Right Icon
- Cross Icon (Small - Medium - Large)
- Check Icon (Small - Medium - Large)
Page 4:
-Photo Gallery Icon
Page 6:
- Icon for describing process step 1: "Choose a Category"
- Icon for describing process step 2: "Reveal It"
- Icon for describing process step 3: "Complete"
-Category Icon for "Relations" category
-Category Icon for "Social" category
-Category Icon for "Technical" category
-Category Icon for "At Home" category
-Category Icon for "Sports" category
-Category Icon for "Outdoors" category
Page 10:
- Home Icon
- Friends Icon
- Add Friends Icon
- About Icon
- Settings Icon
Page 11:
- Hide from Timeline Icon
- Add Friend Icon
Page 12:
- Stealth Mode Icon
Colors
Designer to choose colors to be used in the design.

```html
<!DOCTYPE html>
<html lang="en">
<head>
<meta charset="utf-8">
<title>Pick the Pal – Sliding Panel</title>
<link rel="stylesheet" href="https://fonts.googleapis.com/css2?family=Mulish:wght@400;600&display=swap">
<style>
  :root {
    --page-bg: #c3c6cb;
    --panel: #2f6774;
    --panel-light: #3a7380;
    --panel-band: #2b5f6b;
    --underlay: #4f7c88;
    --underlay-dark: #3d6a76;
    --accent: #35c6dc;
    --text: #f2f6f7;
    --thumb: #6d8a8f;
  }
  * { box-sizing: border-box; margin: 0; padding: 0; }
  html, body { width: 1200px; height: 1195px; overflow: hidden; }
  body {
    background: var(--page-bg);
    font-family: "Mulish", sans-serif;
    color: var(--text);
    position: relative;
  }
  .screen {
    position: absolute;
    left: 310px; top: 82px;
    width: 580px; height: 1030px;
    background: var(--underlay);
    overflow: hidden;
  }
  /* content behind the sliding panel */
  .underlay { position: absolute; left: 470px; top: 0; width: 110px; height: 100%; }
  .status-dots { position: absolute; left: 16px; top: 10px; display: flex; gap: 5px; }
  .status-dots span { width: 8px; height: 8px; border-radius: 50%; background: #d9e6e8; opacity: .8; }
  .menu-toggle {
    position: absolute; left: 30px; top: 28px; width: 52px; height: 52px;
    border-radius: 50%; border: 2px solid #6fb3c0; background: var(--underlay-dark);
  }
  .back-button {
    position: absolute; left: 8px; top: 122px; width: 56px; height: 56px;
    border-radius: 50%; background: #2d6470;
  }
  .percent-label {
    position: absolute; left: 6px; top: 215px; width: 70px; height: 34px;
    background: var(--underlay-dark); color: #a9c4c9; font-size: 18px;
    line-height: 34px; padding-left: 14px;
  }
  .thumb {
    position: absolute; left: 20px; width: 72px; height: 56px;
    background: var(--thumb); border-radius: 4px; opacity: .75;
  }
  /* sliding panel */
  .panel {
    position: absolute; left: 0; top: 0; width: 470px; height: 100%;
    background: linear-gradient(160deg, var(--panel-light) 0%, var(--panel) 55%, var(--panel-light) 100%);
    box-shadow: 6px 0 18px rgba(0,0,0,.25);
  }
  .avatar {
    position: absolute; left: 183px; top: 110px; width: 104px; height: 104px;
    border-radius: 50%; border: 4px solid #8fd3de;
    background: radial-gradient(circle at 50% 40%, #8a7a66, #3c4a3c);
  }
  .user-name {
    position: absolute; left: 0; top: 240px; width: 470px; text-align: center;
    font-size: 34px; font-weight: 600; letter-spacing: .5px;
  }
  .profile-button {
    position: absolute; left: 85px; top: 302px; width: 300px; height: 48px;
    border: 2px solid var(--accent); border-radius: 10px;
    color: var(--accent); font-size: 17px; text-align: center; line-height: 44px;
  }
  .menu { position: absolute; left: 0; top: 400px; width: 470px; list-style: none; }
  .menu-item {
    position: relative; height: 96px; display: flex; align-items: center;
    padding-left: 50px; border-top: 1px solid rgba(255,255,255,.06);
  }
  .menu-item:nth-child(odd) { background: var(--panel-band); }
  .menu-icon { width: 56px; height: 56px; flex: none; }
  .menu-label { margin-left: 44px; font-size: 27px; font-weight: 400; }
  .add-friend {
    position: absolute; right: 30px; top: 28px; height: 38px; padding: 0 16px;
    border: 2px solid var(--accent); border-radius: 8px;
    color: var(--accent); font-size: 16px; line-height: 34px;
  }
</style>
</head>
<body>
  <main class="screen">
    <div class="underlay">
      <div class="status-dots"><span></span><span></span><span></span><span></span><span></span></div>
      <div class="menu-toggle">
        <svg width="48" height="48" viewBox="0 0 48 48"><g stroke="#8cc7d2" stroke-width="3" stroke-linecap="round"><line x1="15" y1="17" x2="33" y2="17"/><line x1="15" y1="24" x2="33" y2="24"/><line x1="15" y1="31" x2="33" y2="31"/></g></svg>
      </div>
      <div class="back-button">
        <svg width="56" height="56" viewBox="0 0 56 56"><polyline points="32,18 22,28 32,38" fill="none" stroke="#cfe3e6" stroke-width="3" stroke-linecap="round"/></svg>
      </div>
      <div class="percent-label">57%</div>
      <div class="thumb" style="top:300px"></div>
      <div class="thumb" style="top:420px"></div>
      <div class="thumb" style="top:540px"></div>
      <div class="thumb" style="top:660px"></div>
      <div class="thumb" style="top:780px"></div>
    </div>

    <nav class="panel">
      <div class="avatar" role="img" aria-label="User profile photo"></div>
      <h1 class="user-name">Dimitris Kalaros</h1>
      <div class="profile-button">View Profile and History</div>
      <ul class="menu">
        <li class="menu-item">
          <svg class="menu-icon" viewBox="0 0 56 56" fill="none" stroke="#fff" stroke-width="3" stroke-linejoin="round">
            <polyline points="6,28 28,8 50,28"/><polyline points="12,24 12,48 44,48 44,24"/>
            <circle cx="28" cy="30" r="5" fill="#fff" stroke="none"/><path d="M19 46c1-7 5-10 9-10s8 3 9 10" fill="#fff" stroke="none"/>
          </svg>
          <span class="menu-label">Home</span>
        </li>
        <li class="menu-item">
          <svg class="menu-icon" viewBox="0 0 56 56" fill="#fff">
            <circle cx="19" cy="18" r="8"/><circle cx="37" cy="16" r="8"/>
            <path d="M5 46c1-12 8-17 14-17s13 5 14 17" fill="none" stroke="#fff" stroke-width="3"/>
            <path d="M31 28c2-1 4-2 6-2 7 0 13 5 14 16" fill="none" stroke="#fff" stroke-width="3"/>
          </svg>
          <span class="menu-label">Friends</span>
          <span class="add-friend">Add Friend</span>
        </li>
        <li class="menu-item">
          <svg class="menu-icon" viewBox="0 0 56 56">
            <circle cx="28" cy="28" r="25" fill="#fff"/>
            <text x="28" y="38" text-anchor="middle" font-family="Mulish, sans-serif" font-weight="600" font-size="28" fill="#2f6774">?</text>
          </svg>
          <span class="menu-label">About</span>
        </li>
        <li class="menu-item">
          <svg class="menu-icon" viewBox="0 0 56 56">
            <g fill="#fff">
              <circle cx="28" cy="28" r="17"/>
              <rect x="24" y="4" width="8" height="10" rx="2"/><rect x="24" y="42" width="8" height="10" rx="2"/>
              <rect x="4" y="24" width="10" height="8" rx="2"/><rect x="42" y="24" width="10" height="8" rx="2"/>
              <rect x="24" y="4" width="8" height="10" rx="2" transform="rotate(45 28 28)"/><rect x="24" y="42" width="8" height="10" rx="2" transform="rotate(45 28 28)"/>
              <rect x="4" y="24" width="10" height="8" rx="2" transform="rotate(45 28 28)"/><rect x="42" y="24" width="10" height="8" rx="2" transform="rotate(45 28 28)"/>
            </g>
            <circle cx="28" cy="28" r="8" fill="#2f6774"/>
          </svg>
          <span class="menu-label">Settings</span>
        </li>
      </ul>
    </nav>
  </main>
</body>
</html>
```